International Automotive Parts Marketing business needs professional, sleek Android app design.

We have developed an Android app for our sales team and are now looking for an overall design our developers can apply. The design should mirror our corporate website kvrl.com. There is a LOT of data the reps need to work through so not really any images other that login screen - of course icons are great. Lots of lists and searches etc. - it needs to look professional, feel amazing and easy to use. Our motto - Simple is always better. We included our logo and a few screenshots of the app page 1 and 2.

Target Market(s)

Professional Sales and Marketing - our own sales team (100 reps) will use this app

Font styles to use
Sans Serif

Colors

Designer to choose colors to be used in the design.

Requirements
Must have
• App design must be professional and easy to use in the field all day. Similar look and feel of corporate website kvrl.com. Same colors and images. Icons to manage navigation
Should not have
• Non-professional look and feel. No vector cartoon type images. No specific parts related images

```html
<!DOCTYPE html>
<html lang="en">
<head>
<meta charset="utf-8">
<title>Vantora Sales App – Screen Set</title>
<link href="https://fonts.googleapis.com/css2?family=Roboto+Condensed:wght@400;700&display=swap" rel="stylesheet">
<style>
:root{
  --stage:#8e8e8e;
  --ink:#000;
  --red:#d50f2f;
  --text:#222;
  --muted:#8a8a8a;
  --line:#dcdcdc;
  --soft:#f2f2f2;
  --info-bg:#eef6fb;
  --info-line:#cfe3f0;
  --info:#3a9fd8;
  --paper:#fff;
}
*{box-sizing:border-box;margin:0;padding:0}
html,body{width:1200px;height:1200px;overflow:hidden;background:var(--stage)}
body{font-family:"Roboto Condensed",Arial,sans-serif;color:var(--text)}
.board{position:absolute;left:0;top:0;width:1932px;height:1932px;transform:scale(0.62112);transform-origin:0 0;background:var(--stage)}
.title{position:absolute;font-size:25px;font-weight:700;color:#f4f4f4}
.screen{position:absolute;width:278px;background:var(--paper);overflow:hidden}
.appbar{position:absolute;left:0;top:0;width:100%;height:46px;background:var(--ink);color:#fff;font-size:11px;font-weight:700;text-align:center;line-height:46px}
.appbar svg{position:absolute;top:15px}
.appbar .l{left:10px}.appbar .r{right:10px}.appbar .r2{right:38px}
.lbl{position:absolute;left:17px;font-size:11px;color:var(--text)}
.field{position:absolute;left:17px;right:17px;height:27px;border:1px solid var(--line);font-size:11px;color:var(--muted);padding-left:6px;line-height:25px;background:#fff}
.field.val{color:var(--text)}
.field.sel::after{content:"";position:absolute;right:8px;top:11px;border:4px solid transparent;border-top:5px solid #888}
.field.cal::after{content:"";position:absolute;right:8px;top:7px;width:10px;height:10px;border:1.5px solid #999;border-top-width:3px;border-radius:1px}
.adv{position:absolute;left:17px;right:17px;height:27px;background:var(--info-bg);border:1px solid var(--info-line);color:var(--info);font-size:11px;line-height:25px;padding-left:7px}
.adv svg{position:absolute;right:8px;top:8px}
.btn{position:absolute;height:30px;background:var(--red);color:#fff;font-size:11px;font-weight:700;text-align:center;line-height:30px}
.check{position:absolute;left:0;width:100%;height:28px;background:var(--soft);font-size:11px;line-height:28px;padding-left:17px;border-bottom:1px solid #e6e6e6}
.box{position:absolute;right:18px;top:7px;width:13px;height:13px;border:1.5px solid #999;background:#fff}
.box.on{background:var(--red);border-color:var(--red)}
.box.on::after{content:"";position:absolute;left:3px;top:0;width:4px;height:7px;border:solid #fff;border-width:0 2px 2px 0;transform:rotate(45deg)}
/* splash & login */
.brand{position:absolute;display:flex;align-items:center;gap:10px;font-size:26px;font-weight:700;letter-spacing:1px}
.brand i{display:block;width:58px;height:58px;border-radius:50%}
.photo{position:absolute}
/* home grid */
.grid{position:absolute;left:8px;top:54px;width:262px;height:429px;display:grid;grid-template-columns:1fr 1fr;grid-template-rows:repeat(3,1fr);border:1px solid #ececec}
.cell{position:relative;border-right:1px solid #ececec;border-bottom:1px solid #ececec;text-align:center;font-size:11px}
.cell svg{position:absolute;left:37px;top:43px}
.cell span{position:absolute;left:0;right:0;top:109px}
.cell.active{background:#fff;box-shadow:0 2px 8px rgba(0,0,0,.25);z-index:2}
.cell.active::after{content:"";position:absolute;left:0;right:0;bottom:0;height:4px;background:var(--red)}
/* lists */
.groupby{position:absolute;left:0;top:47px;width:100%;height:34px;border-bottom:1px solid #e5e5e5;font-size:11px;color:#666;line-height:34px;padding-left:32px}
.card{position:absolute;left:7px;width:264px;height:81px;border:1px solid #e5e5e5;background:#fff;font-size:9px}
.card .nm{position:absolute;left:12px;top:11px;font-size:11px}
.card .ln{position:absolute;left:12px;white-space:nowrap}
.card .chev{position:absolute;right:10px;top:32px}
.pin{display:inline-block;vertical-align:-2px;margin-right:3px}
.modify{position:absolute;left:8px;right:8px;top:457px;height:24px;background:var(--info-bg);border:1px solid var(--info-line);color:var(--info);font-size:11px;line-height:22px;padding-left:8px}
.modify svg{position:absolute;right:8px;top:4px}
/* detail */
.drow{position:absolute;left:50px;font-size:11px;line-height:16px}
.drow small{display:block;font-size:9px;color:var(--muted);line-height:12px}
.dico{position:absolute;left:26px}
.footbar{position:absolute;left:0;bottom:0;width:100%;height:38px;border-top:1px solid #e5e5e5;font-size:11px}
.footbar div{position:absolute;top:6px;line-height:13px}
.footbar small{display:block;font-size:9px;color:var(--muted)}
.dim{position:absolute;inset:46px 0 0 0;background:rgba(0,0,0,.33)}
.modal{position:absolute;left:8px;top:159px;width:262px;height:215px;background:#fff;padding:20px 0 0 19px}
.modal h4{font-size:13px;color:#999;font-weight:700;margin-bottom:16px;letter-spacing:.3px}
.modal p{font-size:13px;line-height:32px}
/* supplier */
.filters{position:absolute;left:0;top:47px;width:100%;height:33px;border-bottom:1px solid #e5e5e5;font-size:11px;color:#999;line-height:33px}
.filters span{position:absolute;top:0}
.showbar{position:absolute;left:7px;right:7px;height:29px;background:var(--info-bg);border:1px solid var(--info-line);color:var(--info);font-size:11px;font-weight:700;text-align:center;line-height:27px}
.scard{position:absolute;left:7px;width:264px;height:103px;border:1px solid #e5e5e5;background:#fff;font-size:9px}
.scard .ln{position:absolute;left:30px;white-space:nowrap}
.scard .ln.t{font-size:10.5px}
.scard .box{left:9px;right:auto;top:8px}
.scard .chev{position:absolute;right:8px;top:42px}
.tabs{position:absolute;left:0;top:47px;width:100%;height:34px;border-bottom:1px solid #e5e5e5;font-size:10.5px}
.tabs span{position:absolute;top:0;width:50%;text-align:center;line-height:32px}
.tabs .on{font-weight:700;border-bottom:3px solid var(--red)}
.ibox{position:absolute;left:7px;right:7px;border:1px solid #e5e5e5}
.summary{position:absolute;left:19px;font-size:9px;white-space:nowrap}
.summary.t{font-size:10.5px}
.list-row{position:absolute;left:7px;right:7px;height:29px;background:var(--soft);border-bottom:1px solid #e3e3e3;font-size:11px;line-height:29px;padding-left:10px}
b{font-weight:700}
</style>
</head>
<body>
<svg width="0" height="0" style="position:absolute">
  <defs>
    <symbol id="ring" viewBox="0 0 56 56"><circle cx="28" cy="28" r="26" fill="none" stroke="currentColor" stroke-width="2.5"/></symbol>
    <symbol id="i-search" viewBox="0 0 56 56"><use href="#ring"/><circle cx="27" cy="26" r="11" fill="none" stroke="currentColor" stroke-width="2.5"/><circle cx="27" cy="26" r="6" fill="none" stroke="currentColor" stroke-width="1.5"/><path d="M19 34 L12 41" stroke="currentColor" stroke-width="3"/></symbol>
    <symbol id="i-route" viewBox="0 0 56 56"><use href="#ring"/><path d="M19 36 C11 27 12 17 19 17 C26 17 27 27 19 36Z M37 36 C29 27 30 17 37 17 C44 17 45 27 37 36Z" fill="none" stroke="currentColor" stroke-width="2.2"/><path d="M15 40 H41" stroke="currentColor" stroke-width="2" stroke-dasharray="3 2"/></symbol>
    <symbol id="i-clients" viewBox="0 0 56 56"><use href="#ring"/><g fill="none" stroke="currentColor" stroke-width="2.2"><circle cx="17" cy="23" r="4"/><circle cx="28" cy="21" r="4.5"/><circle cx="39" cy="23" r="4"/><path d="M10 36 C10 29 24 29 24 36 M21 36 C21 28 35 28 35 36 M32 36 C32 29 46 29 46 36 M10 36 H46"/></g></symbol>
    <symbol id="i-list" viewBox="0 0 56 56"><use href="#ring"/><g fill="none" stroke="currentColor" stroke-width="2.2"><rect x="18" y="15" width="20" height="27" rx="2"/><rect x="23" y="12" width="10" height="6"/><path d="M22 24 H34 M22 29 H34 M22 34 H34 M22 38 H30"/></g></symbol>
    <symbol id="i-partner" viewBox="0 0 56 56"><use href="#ring"/><g fill="none" stroke="currentColor" stroke-width="2.2"><path d="M10 20 H16 V36 H10 M46 20 H40 V36 H46"/><path d="M16 23 L24 20 L32 24 L40 22 M16 33 L22 38 L26 36 L30 39 L34 36 L40 33 M26 26 L30 30"/></g></symbol>
    <symbol id="i-touch" viewBox="0 0 56 56"><use href="#ring"/><g fill="none" stroke="currentColor" stroke-width="2.2"><rect x="15" y="17" width="26" height="23" rx="2"/><path d="M15 23 H41 M21 14 V19 M35 14 V19"/><circle cx="28" cy="32" r="5"/><path d="M25.5 32 L27.5 34 L31 30"/></g></symbol>
    <symbol id="back" viewBox="0 0 16 16"><path d="M14 8 H3 M8 3 L3 8 L8 13" fill="none" stroke="currentColor" stroke-width="1.8"/></symbol>
    <symbol id="dots" viewBox="0 0 16 16"><circle cx="8" cy="3" r="1.5" fill="currentColor"/><circle cx="8" cy="8" r="1.5" fill="currentColor"/><circle cx="8" cy="13" r="1.5" fill="currentColor"/></symbol>
    <symbol id="pencil" viewBox="0 0 16 16"><path d="M2 14 L3 10 L11 2 L14 5 L6 13Z" fill="currentColor"/></symbol>
    <symbol id="mag" viewBox="0 0 16 16"><circle cx="6.5" cy="6.5" r="4.5" fill="none" stroke="currentColor" stroke-width="1.8"/><path d="M10 10 L14.5 14.5" stroke="currentColor" stroke-width="2"/></symbol>
    <symbol id="gear" viewBox="0 0 16 16"><circle cx="8" cy="8" r="5.5" fill="none" stroke="currentColor" stroke-width="3" stroke-dasharray="2.2 1.4"/><circle cx="8" cy="8" r="3.5" fill="none" stroke="currentColor" stroke-width="2"/></symbol>
    <symbol id="chev" viewBox="0 0 10 16"><path d="M2 2 L8 8 L2 14" fill="none" stroke="#777" stroke-width="1.6"/></symbol>
    <symbol id="pinic" viewBox="0 0 10 12"><path d="M5 12 C1 7 0 5 0 4.5 A5 4.5 0 0 1 10 4.5 C10 5 9 7 5 12Z" fill="var(--red)"/><circle cx="5" cy="4.5" r="1.8" fill="#fff"/></symbol>
  </defs>
</svg>

<main class="board">
  <!-- row titles -->
  <h2 class="title" style="left:88px;top:124px">Splash Screen</h2>
  <h2 class="title" style="left:386px;top:124px">Login</h2>
  <h2 class="title" style="left:683px;top:124px">Home</h2>
  <h2 class="title" style="left:981px;top:124px">Click state</h2>
  <h2 class="title" style="left:1278px;top:124px">Search</h2>
  <h2 class="title" style="left:1576px;top:124px">Advance Search</h2>
  <h2 class="title" style="left:88px;top:1203px">Company List</h2>
  <h2 class="title" style="left:386px;top:1203px">Company Detail</h2>
  <h2 class="title" style="left:683px;top:1203px">Choose option</h2>
  <h2 class="title" style="left:981px;top:1203px">Supplier List</h2>
  <h2 class="title" style="left:1278px;top:1203px">Sales Information</h2>
  <h2 class="title" style="left:1576px;top:1203px">Action Alert</h2>

  <!-- Splash -->
  <section class="screen splash" style="left:88px;top:168px;height:494px;background:#000">
    <div class="brand" style="left:22px;top:113px;color:#fff"><i style="background:#fff"></i>VANTORA</div>
    <div class="photo" role="img" aria-label="Photo of a black luxury car front" style="left:0;top:212px;width:278px;height:178px;background:radial-gradient(ellipse at 60% 60%,#6d6d6d 0%,#2a2a2a 45%,#050505 80%)"></div>
    <div class="photo" role="img" aria-label="Close-up of a car dashboard climate dial" style="left:0;top:390px;width:139px;height:104px;background:linear-gradient(135deg,#3b3b3b,#8f8a80 50%,#2c2c2c)"></div>
    <div class="photo" role="img" aria-label="Close-up of a car gear lever" style="left:139px;top:390px;width:139px;height:104px;background:linear-gradient(135deg,#595959,#1e1e1e 60%,#7a7a7a)"></div>
  </section>

  <!-- Login -->
  <section class="screen login" style="left:386px;top:168px;height:494px">
    <div class="brand" style="left:22px;top:113px;color:#111"><i style="background:var(--red)"></i>VANTORA</div>
    <div style="position:absolute;left:20px;top:238px;font-size:14px;font-weight:700">LOGIN</div>
    <div class="field" style="left:21px;right:21px;top:267px">Enter username</div>
    <div class="field" style="left:21px;right:21px;top:302px">Enter password</div>
    <div class="btn" style="left:21px;right:20px;top:344px;width:auto">LOGIN</div>
  </section>

  <!-- Home -->
  <section class="screen home" style="left:683px;top:168px;height:494px">
    <header class="appbar"><svg class="l" width="18" height="18"><circle cx="9" cy="9" r="9" fill="var(--red)"/></svg>HOME<svg class="r" width="16" height="16" style="color:#fff"><use href="#gear"/></svg></header>
    <div class="grid">
      <div class="cell"><svg width="56" height="56"><use href="#i-search"/></svg><span>SEARCH</span></div>
      <div class="cell"><svg width="56" height="56"><use href="#i-route"/></svg><span>ROUTE</span></div>
      <div class="cell"><svg width="56" height="56"><use href="#i-clients"/></svg><span>MY CLIENTS</span></div>
      <div class="cell"><svg width="56" height="56"><use href="#i-list"/></svg><span>CUSTOM LIST</span></div>
      <div class="cell"><svg width="56" height="56"><use href="#i-partner"/></svg><span>PARTNER</span></div>
      <div class="cell"><svg width="56" height="56"><use href="#i-touch"/></svg><span>MARKET TOUCHES</span></div>
    </div>
  </section>

  <!-- Click state -->
  <section class="screen home" style="left:981px;top:168px;height:494px">
    <header class="appbar"><svg class="l" width="18" height="18"><circle cx="9" cy="9" r="9" fill="var(--red)"/></svg>HOME<svg class="r" width="16" height="16" style="color:#fff"><use href="#gear"/></svg></header>
    <div class="grid">
      <div class="cell active"><svg width="56" height="56" style="color:#fff"><circle cx="28" cy="28" r="28" fill="var(--red)"/><use href="#i-search"/></svg><span>SEARCH</span></div>
      <div class="cell"><svg width="56" height="56"><use href="#i-route"/></svg><span>ROUTE</span></div>
      <div class="cell"><svg width="56" height="56"><use href="#i-clients"/></svg><span>MY CLIENTS</span></div>
      <div class="cell"><svg width="56" height="56"><use href="#i-list"/></svg><span>CUSTOM LIST</span></div>
      <div class="cell"><svg width="56" height="56"><use href="#i-partner"/></svg><span>PARTNER</span></div>
      <div class="cell"><svg width="56" height="56"><use href="#i-touch"/></svg><span>MARKET TOUCHES</span></div>
    </div>
  </section>

  <!-- Search -->
  <section class="screen search" style="left:1278px;top:168px;height:494px">
    <header class="appbar"><svg class="l" width="16" height="16" style="color:#fff"><use href="#back"/></svg>SEARCH</header>
    <div class="lbl" style="top:70px">Company name</div><div class="field" style="top:91px">Enter</div>
    <div class="lbl" style="top:138px">Type</div><div class="field" style="top:158px">Enter</div>
    <div class="lbl" style="top:201px">Ratings</div><div class="field sel val" style="top:222px">All</div>
    <div class="lbl" style="top:265px">Location</div><div class="field" style="top:286px">Enter</div>
    <div class="adv" style="top:325px">ADVANCE SEARCH<svg width="12" height="8"><path d="M1 1 L6 6 L11 1" fill="none" stroke="var(--info)" stroke-width="1.6"/></svg></div>
    <div class="btn" style="left:17px;width:244px;top:367px">SEARCH</div>
    <div class="btn" style="left:17px;width:120px;top:402px">MY CLIENTS</div>
    <div class="btn" style="left:142px;width:119px;top:402px">ADD COMPANY</div>
  </section>

  <!-- Advance search -->
  <section class="screen search" style="left:1576px;top:168px;height:905px">
    <header class="appbar"><svg class="l" width="16" height="16" style="color:#fff"><use href="#back"/></svg>SEARCH</header>
    <div class="lbl" style="top:70px">Company name</div><div class="field" style="top:91px">Enter</div>
    <div class="lbl" style="top:138px">Type</div><div class="field" style="top:158px">Enter</div>
    <div class="lbl" style="top:201px">Ratings</div><div class="field sel val" style="top:222px">All</div>
    <div class="lbl" style="top:265px">Location</div><div class="field" style="top:286px">Enter</div>
    <div class="adv" style="top:325px">ADVANCE SEARCH<svg width="12" height="8"><path d="M1 7 L6 2 L11 7" fill="none" stroke="var(--info)" stroke-width="1.6"/></svg></div>
    <div class="lbl" style="top:367px">Market</div><div class="field sel val" style="top:388px">All</div>
    <div class="lbl" style="top:431px">Franchise</div><div class="field sel val" style="top:452px">All</div>
    <div class="lbl" style="top:495px">LOI</div><div class="field sel val" style="top:516px">None</div>
    <div class="check" style="top:559px">Rewards<span class="box"></span></div>
    <div class="check" style="top:588px">My Touchs<span class="box on"></span></div>
    <div class="lbl" style="top:633px">Touch start</div><div class="field cal val" style="top:653px">All</div>
    <div class="lbl" style="top:697px">Touch end</div><div class="field cal val" style="top:717px">All</div>
    <div class="lbl" style="top:760px">Sales type</div><div class="field sel val" style="top:781px">None</div>
    <div class="btn" style="left:17px;width:244px;top:824px">SEARCH</div>
    <div class="btn" style="left:17px;width:120px;top:859px">MY CLIENTS</div>
    <div class="btn" style="left:142px;width:119px;top:859px">ADD COMPANY</div>
  </section>

  <!-- Company list -->
  <section class="screen clist" style="left:88px;top:1247px;height:494px">
    <header class="appbar"><svg class="l" width="16" height="16"><path d="M8 2 L15 8 H13 V14 H3 V8 H1Z" fill="#fff"/></svg>COMPANY LIST<svg class="r" width="16" height="16"><path d="M1 3 H15 M1 8 H15 M1 13 H15 M10 1 V5 M5 6 V10 M11 11 V15" stroke="#fff" stroke-width="1.6"/></svg></header>
    <div class="groupby"><svg width="14" height="10" style="position:absolute;left:9px;top:12px"><path d="M0 1 H14 M0 5 H10 M0 9 H6" stroke="#777" stroke-width="1.4"/></svg>Group by<svg width="10" height="6" style="position:absolute;right:8px;top:14px"><path d="M0 0 H10 L5 6Z" fill="#888"/></svg></div>
    <article class="card" style="top:90px"><div class="nm">LANE 12 AUTO SERVICE CENTRE</div><div class="ln" style="top:28px"><svg class="pin" width="8" height="10"><use href="#pinic"/></svg>Brookdale BC</div><div class="ln" style="top:43px">Type : <b>M</b> &nbsp;| &nbsp;Rating : <b>B</b></div><div class="ln" style="top:58px">Last Touch : <b>05-Apr-2012</b></div><svg class="chev" width="10" height="16"><use href="#chev"/></svg></article>
    <article class="card" style="top:171px"><div class="nm">FIRST MILE AUTOMOTIVE</div><div class="ln" style="top:28px"><svg class="pin" width="8" height="10"><use href="#pinic"/></svg>Brookdale BC</div><div class="ln" style="top:43px">Type : <b>M</b> &nbsp;| &nbsp;Rating : <b>B</b></div><div class="ln" style="top:58px">Last Touch : <b>05-Apr-2012</b></div><svg class="chev" width="10" height="16"><use href="#chev"/></svg></article>
    <article class="card" style="top:252px"><div class="nm">METRO AUTO COLLISION</div><div class="ln" style="top:28px"><svg class="pin" width="8" height="10"><use href="#pinic"/></svg>Brookdale BC</div><div class="ln" style="top:43px">Type : <b>M</b> &nbsp;| &nbsp;Rating : <b>B</b></div><div class="ln" style="top:58px">Last Touch : <b>05-Apr-2012</b></div><svg class="chev" width="10" height="16"><use href="#chev"/></svg></article>
    <article class="card" style="top:333px"><div class="nm">ALL HOURS COLLISION CENTRE</div><div class="ln" style="top:28px"><svg class="pin" width="8" height="10"><use href="#pinic"/></svg>Brookdale BC</div><div class="ln" style="top:43px">Type : <b>M</b> &nbsp;| &nbsp;Rating : <b>B</b></div><div class="ln" style="top:58px">Last Touch : <b>05-Apr-2012</b></div><svg class="chev" width="10" height="16"><use href="#chev"/></svg></article>
    <article class="card" style="top:414px"><div class="nm">LANE 12 AUTO SERVICE CENTRE</div><div class="ln" style="top:28px"><svg class="pin" width="8" height="10"><use href="#pinic"/></svg>Brookdale BC</div><svg class="chev" width="10" height="16"><use href="#chev"/></svg></article>
    <div class="modify">MODIFY SEARCH<svg width="14" height="14" style="color:var(--info)"><use href="#mag"/></svg></div>
  </section>

  <!-- Company detail -->
  <section class="screen detail" style="left:386px;top:1247px;height:494px">
    <header class="appbar"><svg class="l" width="16" height="16" style="color:#fff"><use href="#back"/></svg>COMPANY INFO<svg class="r2" width="16" height="16" style="color:#fff"><use href="#pencil"/></svg><svg class="r" width="16" height="16" style="color:#fff"><use href="#dots"/></svg></header>
    <svg class="dico" width="11" height="11" style="top:66px"><rect width="11" height="11" fill="var(--red)"/></svg><div class="drow" style="top:66px"><small>Company Name</small><b>LANE 12 AUTO SERVICE CENTRE</b></div>
    <svg class="dico" width="10" height="12" style="top:110px"><use href="#pinic"/></svg><div class="drow" style="top:110px"><small>Address, Location &amp; Zip code</small>412 B Cedar RD<br>Brookdale BC<br>Canada V2M 4K1</div>
    <svg class="dico" width="11" height="11" style="top:186px"><rect width="11" height="11" rx="1" fill="var(--red)"/></svg><div class="drow" style="top:186px"><small>Fax</small>604-5550142</div>
    <svg class="dico" width="11" height="11" style="top:229px"><rect width="11" height="9" fill="var(--red)"/></svg><div class="drow" style="top:229px"><small>Type</small>M</div>
    <svg class="dico" width="11" height="11" style="top:272px"><rect width="11" height="11" fill="var(--red)"/></svg><div class="drow" style="top:272px"><small>Rating</small>B</div>
    <svg class="dico" width="11" height="11" style="top:316px"><rect width="11" height="9" fill="var(--red)"/></svg><div class="drow" style="top:316px"><small>Comment</small>N/A</div>
    <svg class="dico" width="12" height="8" style="top:359px"><rect width="12" height="8" fill="var(--red)"/></svg><div class="drow" style="top:359px"><small>Partner</small>Crestline Authorized Repairs</div>
    <svg class="dico" width="12" height="8" style="top:402px"><rect width="12" height="8" fill="var(--red)"/></svg><div class="drow" style="top:402px"><small>Franchise</small>N/A</div>
    <footer class="footbar"><svg width="12" height="12" style="position:absolute;left:12px;top:13px"><path d="M2 1 L5 1 L6 4 L4 5 C5 7 6 8 8 9 L9 7 L12 8 V11 C6 12 0 6 1 1Z" fill="var(--red)"/></svg><div style="left:34px"><small>Phone</small>604-5550142</div><span style="position:absolute;left:138px;top:0;bottom:0;border-left:1px solid #e5e5e5"></span><svg width="13" height="10" style="position:absolute;left:150px;top:14px"><rect width="13" height="10" fill="var(--red)"/><path d="M0 0 L6.5 5 L13 0" fill="none" stroke="#fff" stroke-width="1.2"/></svg><div style="left:173px"><small>Email</small>info@lane12auto.com</div></footer>
  </section>

  <!-- Choose option -->
  <section class="screen detail" style="left:683px;top:1247px;height:532px">
    <header class="appbar"><svg class="l" width="16" height="16" style="color:#fff"><use href="#back"/></svg>COMPANY INFO<svg class="r2" width="16" height="16" style="color:#fff"><use href="#pencil"/></svg><svg class="r" width="16" height="16" style="color:#fff"><use href="#dots"/></svg></header>
    <svg class="dico" width="11" height="11" style="top:66px"><rect width="11" height="11" fill="var(--red)"/></svg><div class="drow" style="top:66px"><small>Company Name</small><b>LANE 12 AUTO SERVICE CENTRE</b></div>
    <svg class="dico" width="10" height="12" style="top:110px"><use href="#pinic"/></svg><div class="drow" style="top:110px"><small>Address, Location &amp; Zip code</small>412 B Cedar RD<br>Brookdale BC</div>
    <div class="drow" style="top:370px">B</div>
    <svg class="dico" width="11" height="11" style="top:402px"><rect width="11" height="9" fill="var(--red)"/></svg><div class="drow" style="top:402px"><small>Comment</small>N/A</div>
    <svg class="dico" width="12" height="8" style="top:445px"><rect width="12" height="8" fill="var(--red)"/></svg><div class="drow" style="top:445px"><small>Partner</small>Crestline Authorized Repairs</div>
    <svg class="dico" width="12" height="8" style="top:488px"><rect width="12" height="8" fill="var(--red)"/></svg><div class="drow" style="top:488px"><small>Franchise</small>N/A</div>
    <div class="dim"></div>
    <div class="modal"><h4>CHOOSE ONE</h4><p>Contact</p><p>Touches</p><p>Alerts</p><p>Rewards</p><p>Suppliers</p></div>
  </section>

  <!-- Supplier list -->
  <section class="screen supp" style="left:981px;top:1247px;height:494px">
    <header class="appbar"><svg class="l" width="16" height="16" style="color:#fff"><use href="#back"/></svg>SUPPLIERS LIST<svg class="r2" width="15" height="15" style="color:#fff"><use href="#mag"/></svg><svg class="r" width="16" height="16" style="color:#fff"><use href="#dots"/></svg></header>
    <div class="filters"><span style="left:8px">Enter Parts</span><span style="left:138px;right:0;border-left:1px solid #e5e5e5;padding-left:8px">Enter Represented</span></div>
    <div class="showbar" style="top:85px">SHOW DATA</div>
    <article class="scard" style="top:130px"><span class="box on"></span><div class="ln t" style="top:7px">OEM PARTS &nbsp;| &nbsp;AURELO &nbsp;| &nbsp;<svg class="pin" width="8" height="10"><use href="#pinic"/></svg><span style="font-size:9px">Brookdale BC</span></div><div class="ln" style="top:24px">LOI : <b>1</b> &nbsp;| &nbsp;Dis(%) : <b>0</b> &nbsp;| &nbsp;Vol : <b>200</b></div><div class="ln" style="top:46px">Contact : <b>Sam Parts Buyer</b></div><div class="ln" style="top:61px">Touch : <b>12-Dec-2019</b> &nbsp;| &nbsp;Supplier : <b>Harbour Aurelo</b></div><div class="ln" style="top:83px">Comment : <b>Need to replace parts</b></div><svg class="chev" width="10" height="16"><use href="#chev"/></svg></article>
    <article class="scard" style="top:234px"><span class="box"></span><div class="ln t" style="top:7px">OEM PARTS &nbsp;| &nbsp;AURELO &nbsp;| &nbsp;<svg class="pin" width="8" height="10"><use href="#pinic"/></svg><span style="font-size:9px">Brookdale BC</span></div><div class="ln" style="top:24px">LOI : <b>1</b> &nbsp;| &nbsp;Dis(%) : <b>0</b> &nbsp;| &nbsp;Vol : <b>200</b></div><div class="ln" style="top:46px">Contact : <b>Sam Parts Buyer</b></div><div class="ln" style="top:61px">Touch : <b>12-Dec-2019</b> &nbsp;| &nbsp;Supplier : <b>Harbour Aurelo</b></div><div class="ln" style="top:83px">Comment : <b>Need to replace parts</b></div><svg class="chev" width="10" height="16"><use href="#chev"/></svg></article>
    <article class="scard" style="top:338px"><span class="box"></span><div class="ln t" style="top:7px">OEM PARTS &nbsp;| &nbsp;AURELO &nbsp;| &nbsp;<svg class="pin" width="8" height="10"><use href="#pinic"/></svg><span style="font-size:9px">Brookdale BC</span></div><div class="ln" style="top:24px">LOI : <b>1</b> &nbsp;| &nbsp;Dis(%) : <b>0</b> &nbsp;| &nbsp;Vol : <b>200</b></div><div class="ln" style="top:46px">Contact : <b>Sam Parts Buyer</b></div><div class="ln" style="top:61px">Touch : <b>12-Dec-2019</b> &nbsp;| &nbsp;Supplier : <b>Harbour Aurelo</b></div><div class="ln" style="top:83px">Comment : <b>Need to replace parts</b></div><svg class="chev" width="10" height="16"><use href="#chev"/></svg></article>
    <article class="scard" style="top:442px"><span class="box"></span><div class="ln t" style="top:7px">OEM PARTS &nbsp;| &nbsp;AURELO &nbsp;| &nbsp;<svg class="pin" width="8" height="10"><use href="#pinic"/></svg><span style="font-size:9px">Brookdale BC</span></div></article>
    <div class="btn" style="left:0;width:138px;top:456px;height:38px;line-height:38px">COMMON COMMENT</div>
    <div class="btn" style="left:139px;width:139px;top:456px;height:38px;line-height:38px">SEND ACTION ALERTS</div>
  </section>

  <!-- Sales information -->
  <section class="screen sales" style="left:1278px;top:1247px;height:511px">
    <header class="appbar"><svg class="l" width="16" height="16" style="color:#fff"><use href="#back"/></svg>SUPPLIERS LIST<svg class="r" width="16" height="16" style="color:#fff"><use href="#dots"/></svg></header>
    <nav class="tabs"><span class="on" style="left:0">SALES INFORMATION</span><span style="left:50%">ACTION ALERT</span></nav>
    <div class="ibox" style="top:90px;height:338px"></div>
    <div class="summary t" style="top:101px">OEM PARTS &nbsp;| &nbsp;AURELO &nbsp;| &nbsp;<svg class="pin" width="8" height="10"><use href="#pinic"/></svg><span style="font-size:9px">Brookdale BC</span></div>
    <div class="summary" style="top:118px">Contact : <b>Sam Parts Buyer</b></div>
    <div class="summary" style="top:132px">Touch : <b>12-Dec-2019</b> &nbsp;| &nbsp;Supplier : <b>Harbour Aurelo</b></div>
    <div class="summary" style="top:146px">Comment : <b>Need to replace parts</b></div>
    <div class="lbl" style="top:174px">Discount (%)</div><div class="field val" style="top:194px">15</div>
    <div class="lbl" style="top:241px">Level</div><div class="field val" style="top:262px">4</div>
    <div class="lbl" style="top:305px">Monthly Volume</div><div class="field val" style="top:326px">10000</div>
    <div class="lbl" style="top:369px">Comment</div><div class="field" style="top:390px">Enter</div>
    <div class="showbar" style="top:436px">SHOW HISTORY</div>
    <div class="btn" style="left:0;width:278px;top:474px;height:37px;line-height:37px">SAVE</div>
  </section>

  <!-- Action alert -->
  <section class="screen alert" style="left:1576px;top:1247px;height:553px">
    <header class="appbar"><svg class="l" width="16" height="16" style="color:#fff"><use href="#back"/></svg>SUPPLIERS LIST<svg class="r" width="16" height="16" style="color:#fff"><use href="#dots"/></svg></header>
    <nav class="tabs"><span style="left:0">SALES INFORMATION</span><span class="on" style="left:50%">ACTION ALERT</span></nav>
    <div class="ibox" style="top:87px;height:428px"></div>
    <div class="list-row" style="top:90px">Email</div>
    <div class="list-row" style="top:119px">Fax</div>
    <div class="list-row" style="top:148px">SMS</div>
    <div class="lbl" style="top:192px">To</div><div class="field val" style="top:214px">Harbour Aurelo</div>
    <div class="lbl" style="top:260px">Email</div><div class="field val" style="top:281px">test@mail.com</div>
    <div class="lbl" style="top:323px">Cc</div><div class="field" style="top:345px">Enter email</div>
    <div class="lbl" style="top:387px">Phone</div><div class="field" style="top:409px">Enter</div>
    <div class="lbl" style="top:451px">Fax</div><div class="field" style="top:472px">Enter</div>
    <div class="btn" style="left:0;width:92px;top:515px;height:38px;line-height:38px">CANCEL</div>
    <div class="btn" style="left:93px;width:92px;top:515px;height:38px;line-height:38px">PREVIEW</div>
    <div class="btn" style="left:186px;width:92px;top:515px;height:38px;line-height:38px">SEND</div>
  </section>
</main>
</body>
</html>
```